Website redesign

We need a bold revamp of our website (http://www.brantwoodpower.co.nz/)
which at the moment looks dated. We want a crisp, fresh and bold look. The background image behind web page can go. Open to complete new layout

Target Market(s)

Electrical contracting company- working in the domestic and commercial field

Coding

Coded - Design and coding required

Number of Pages Required

5+ page

Font styles to use
Sans Serif

Colors

Designer to choose colors to be used in the design.

```html
<!DOCTYPE html>
<html lang="en">
<head>
<meta charset="utf-8">
<title>Brantwood Power – Home</title>
<link href="https://fonts.googleapis.com/css2?family=Roboto+Condensed:wght@400;700&family=Open+Sans:wght@400;600;700&display=swap" rel="stylesheet">
<style>
:root{
  --red:#e30613;
  --red-dark:#b8050f;
  --ink:#222;
  --text:#666;
  --muted:#999;
  --ghost:#ececec;
  --light:#f0f0f0;
  --hero-a:#e9e9e9;
  --hero-b:#d2d2d2;
  --panel:#efefef;
  --footer:#3a3a3a;
  --footer-deep:#262626;
  --white:#fff;
  --stage:#f3f3f3;
}
*{box-sizing:border-box;margin:0;padding:0}
html,body{width:1200px;height:3516px;overflow:hidden}
body{background:var(--stage);font-family:"Open Sans",sans-serif;color:var(--text);position:relative}
.abs{position:absolute}
.page{position:absolute;left:33px;top:33px;width:1134px;height:2636px;background:var(--white);box-shadow:0 0 14px rgba(0,0,0,.12);overflow:hidden}
.page > *{position:absolute}
.condensed{font-family:"Roboto Condensed",sans-serif}

/* top bar */
.topbar{left:0;top:0;width:1134px;height:37px;border-bottom:1px solid #e5e5e5;font-size:11px;font-weight:700;color:var(--ink)}
.topbar .item{position:absolute;top:11px;display:flex;align-items:center;gap:6px}
.social{display:flex;gap:9px}
.social span{width:10px;height:10px;border-radius:50%;background:var(--red);display:block}

/* nav */
.nav{left:0;top:37px;width:1134px;height:75px}
.logo{position:absolute;display:flex;align-items:center;gap:6px;font-family:"Roboto Condensed",sans-serif;font-weight:700;color:var(--ink);line-height:1}
.logo .mark{width:14px;height:14px;background:var(--red);flex:none}
.nav .logo{left:154px;top:20px;font-size:22px;width:130px;flex-wrap:nowrap}
.nav-link{position:absolute;top:0;height:75px;line-height:75px;font-size:10px;font-weight:600;color:var(--ink);text-transform:uppercase}
.nav-link.active{background:var(--red);color:var(--white);padding:0 12px}
.free-phone{left:802px;top:0;width:178px;height:66px;background:var(--red);color:var(--white);padding:14px 14px;font-size:11px;font-weight:700;line-height:1.6}
.free-phone small{font-size:10px;font-weight:600}

/* hero */
.hero{left:0;top:112px;width:1134px;height:441px;background:linear-gradient(180deg,var(--hero-a),var(--hero-b));border-bottom:3px solid var(--red)}
.hero-art{position:absolute;left:37px;top:31px;width:434px;height:258px;background:radial-gradient(ellipse at 60% 45%,#cfcfcf,rgba(210,210,210,0) 70%)}
.hero h1{position:absolute;right:154px;top:100px;text-align:right;font-family:"Roboto Condensed",sans-serif;font-weight:700;font-size:50px;line-height:58px;color:#1e1e1e;text-transform:uppercase}
.hero p{position:absolute;right:154px;top:230px;width:400px;text-align:right;font-size:12px;font-weight:700;color:#555;line-height:20px}
.btn-pill{position:absolute;right:154px;top:293px;width:123px;height:33px;border-radius:17px;background:var(--white);display:flex;align-items:center;padding-left:20px;font-size:10px;font-weight:700;color:var(--ink)}
.btn-pill .arrow{position:absolute;right:2px;top:2px;width:29px;height:29px;border-radius:50%;background:var(--red);display:flex;align-items:center;justify-content:center}
.dots{position:absolute;left:529px;top:390px;display:flex;gap:8px}
.dots span{width:16px;height:3px;background:#888;display:block}

/* section headings */
.ghost{font-family:"Roboto Condensed",sans-serif;font-weight:700;color:var(--ghost);text-align:center;width:1134px;left:0}
.heading{font-family:"Roboto Condensed",sans-serif;font-weight:700;color:var(--ink);text-align:center;width:1134px;left:0}

/* about */
.about-ghost{top:595px;font-size:56px}
.about-title{top:622px;font-size:26px}
.tagline{left:420px;top:676px;width:294px;height:16px;border-left:4px solid var(--red);font-size:9px;font-weight:700;color:var(--ink);text-align:center;line-height:16px}
.about-text{left:167px;top:705px;width:808px;text-align:center;font-size:10.5px;line-height:22px;color:var(--muted)}
.divider{left:0;top:834px;width:1134px;height:1px;background:#e3e3e3}

/* services */
.services-ghost{top:855px;font-size:44px}
.services-title{top:878px;font-size:22px;font-weight:400}
.service-panel{left:553px;top:1029px;width:368px;height:309px;background:var(--panel)}
.service-detail{left:616px;top:1085px;width:300px}
.service-detail h3{font-family:"Roboto Condensed",sans-serif;font-size:18px;color:var(--ink);display:flex;align-items:center;gap:12px;margin-bottom:18px}
.service-detail h3::after{content:"";width:44px;height:2px;background:var(--ink)}
.service-detail p{font-size:10.5px;line-height:20px;color:var(--muted)}
.service-card{left:213px;top:944px;width:378px;height:366px;background:var(--red);box-shadow:0 6px 14px rgba(0,0,0,.2)}
.service-card h2{position:absolute;left:14px;top:50px;font-size:18px;font-weight:700;color:var(--white);display:flex;align-items:center;gap:10px}
.service-card h2::after{content:"";width:60px;height:2px;background:var(--white)}
.service-grid{position:absolute;left:24px;top:96px;width:330px;height:204px;display:grid;grid-template-columns:repeat(3,1fr);grid-template-rows:repeat(2,1fr)}
.service-tile{display:flex;flex-direction:column;align-items:center;justify-content:center;gap:10px;color:var(--white);font-size:12px;font-weight:600;border-right:1px solid rgba(255,255,255,.45);border-bottom:1px solid rgba(255,255,255,.45)}
.service-tile:nth-child(3n){border-right:none}
.service-tile:nth-child(n+4){border-bottom:none}
.service-tile.current{background:var(--red-dark)}

/* projects */
.projects{left:0;top:1408px;width:1134px;height:594px;background:linear-gradient(135deg,#4a4a4a,#232323 55%,#3d2a2a)}
.projects-ghost{top:1467px;font-size:44px;color:rgba(255,255,255,.12)}
.projects-title{top:1492px;font-size:21px;color:var(--white)}
.project{width:262px;height:184px;background:linear-gradient(180deg,#c7d3de 0%,#b9c3cc 45%,#8a8f86 70%,#6f7a5e 100%)}
.project-card{left:436px;top:1545px;width:262px;height:184px;background:var(--white);padding:35px 22px 0;text-align:center}
.project-card .badge{width:16px;height:16px;background:var(--red);margin:0 auto 10px}
.project-card h4{font-family:"Roboto Condensed",sans-serif;font-size:17px;color:var(--ink);margin-bottom:10px}
.project-card p{font-size:11px;line-height:19px;color:#444;border-bottom:1px solid #ddd;padding-bottom:8px}

/* newsletter */
.newsletter-head{left:180px;top:2042px;width:174px;text-align:right;border-right:4px solid var(--red);padding-right:10px}
.newsletter-head h3{font-family:"Roboto Condensed",sans-serif;font-size:19px;color:var(--ink)}
.newsletter-head p{font-size:8.5px;font-weight:700;color:#555}
.newsletter-field{left:384px;top:2048px;width:591px;height:42px;border-radius:21px;border:1px solid #ddd;box-shadow:0 2px 5px rgba(0,0,0,.08);font-size:10px;color:#888;padding-left:22px;line-height:40px}
.newsletter-field .send{position:absolute;right:4px;top:4px;width:32px;height:32px;border-radius:50%;background:var(--red);display:flex;align-items:center;justify-content:center}

/* footer */
.footer{left:0;top:2147px;width:1134px;height:445px;background:var(--footer)}
.footer .logo-box{position:absolute;left:154px;top:42px;width:129px;height:75px;background:var(--white);display:flex;align-items:center;justify-content:center}
.footer .logo{position:static;font-size:17px;gap:5px}
.footer-about{position:absolute;left:312px;top:48px;width:668px;font-size:10.5px;line-height:21px;color:#8a8a8a}
.contact{position:absolute;top:164px;display:flex;gap:12px;font-size:10.5px;line-height:16px;color:#9a9a9a}
.contact svg{flex:none;margin-top:2px}
.footer-social{position:absolute;left:851px;top:168px;display:flex;gap:8px}
.footer-social span{width:24px;height:24px;border-radius:50%;border:1px solid #777;display:block}
.quick-title{position:absolute;left:154px;top:262px;font-size:10px;font-weight:700;color:var(--white)}
.links{position:absolute;top:293px;list-style:none;font-size:10px;line-height:26px;color:#9a9a9a}
.copyright{left:0;top:2592px;width:1134px;height:44px;background:var(--footer-deep);font-size:10px;color:#9a9a9a;display:flex;justify-content:space-between;align-items:center;padding:0 154px}

/* device view heading */
.device-heading{left:187px;top:2758px;width:826px;height:64px;display:flex;align-items:center;justify-content:center}
.device-heading::before,.device-heading::after{content:"";position:absolute;top:0;height:3px;background:#111}
.device-heading::before{left:0;width:826px}
.device-heading span{font-family:"Roboto Condensed",sans-serif;font-size:46px;letter-spacing:18px;color:#111;background:var(--stage);padding:0 20px;margin-top:18px}
</style>
</head>
<body>
<div class="page">

  <header class="topbar">
    <div class="item" style="left:154px">
      <svg width="14" height="10" viewBox="0 0 14 10"><rect width="14" height="10" rx="2" fill="#e30613"/><path d="M1 1l6 5 6-5" stroke="#fff" fill="none" stroke-width="1.3"/></svg>
      office@brantwoodpower.co.nz
    </div>
    <div class="item" style="left:342px">
      <svg width="12" height="12" viewBox="0 0 12 12"><path d="M6 0L0 5h2v7h3V8h2v4h3V5h2z" fill="#e30613"/></svg>
      14 Kestrel Street, Wanganui 4500
    </div>
    <div class="item" style="left:834px">Follow Us :
      <div class="social"><span></span><span></span><span></span><span></span></div>
    </div>
  </header>

  <nav class="nav">
    <div class="logo"><span class="mark"></span>Brantwood Power</div>
    <a class="nav-link active" style="left:302px">Home</a>
    <a class="nav-link" style="left:377px">About Us</a>
    <a class="nav-link" style="left:459px">Services</a>
    <a class="nav-link" style="left:546px">Projects</a>
    <a class="nav-link" style="left:630px">Contact Us</a>
    <a class="nav-link" style="left:729px">Info</a>
    <div class="free-phone">FREE PHONE :<br><small>0800 55 21 40 OR (06) 344 7120</small></div>
  </nav>

  <section class="hero">
    <div class="hero-art" role="img" aria-label="Line illustration of a meter, switchboard, warning sign, plug and glowing light bulb"></div>
    <h1>Proudly Serving<br>Our Local Community</h1>
    <p>Brantwood Power is a leading electrical installation and maintenance company based in Wanganui, but servicing all New Zealand.</p>
    <div class="btn-pill">CONTACT US
      <span class="arrow"><svg width="12" height="10" viewBox="0 0 12 10"><path d="M0 5h10M6 1l4 4-4 4" stroke="#fff" stroke-width="1.8" fill="none"/></svg></span>
    </div>
    <div class="dots"><span></span><span></span><span></span></div>
  </section>

  <div class="ghost about-ghost">ABOUT US</div>
  <h2 class="heading about-title">ABOUT US</h2>
  <div class="tagline">PROUDLY SERVING OUR LOCAL COMMUNITY FOR OVER 20 YEARS</div>
  <p class="about-text">Brantwood Power is a leading electrical installation and maintenance company based in Wanganui, but servicing all New Zealand. We are proud to be locally owned and operated. With over 15 employees, we are a very professional qualified and experienced team of technicians and support staff. Brantwood Power was established in 1991 and does it all, from supplying and changing light bulbs, comprehensive whole house electrical design and installation, to commercial and large scale industrial consultation, implementation and servicing.</p>
  <div class="divider"></div>

  <div class="ghost services-ghost">Our Services</div>
  <h2 class="heading services-title">Our Services</h2>
  <div class="service-panel"></div>
  <div class="service-detail">
    <h3>Alarms</h3>
    <p>Brantwood Power offers all the domestic and commercial electrical services you would expect from an electrical firm, but with dedicated technicians in specialist electrical areas they have the more technical ability and experience than your average sparky. If you can't find what you are looking for in the appropriate sections listed, simply contact us on 0800 55 21 40 and we will be able to help you out.</p>
  </div>
  <div class="service-card">
    <h2>Brantwood Power Services.</h2>
    <div class="service-grid">
      <div class="service-tile current">
        <svg width="40" height="30" viewBox="0 0 40 30"><rect x="2" y="4" width="36" height="22" rx="2" fill="none" stroke="#fff" stroke-width="2"/><rect x="8" y="10" width="10" height="10" fill="#fff"/><circle cx="28" cy="15" r="4" fill="#fff"/></svg>Alarms</div>
      <div class="service-tile">
        <svg width="34" height="34" viewBox="0 0 34 34"><circle cx="17" cy="17" r="16" fill="#fff"/><path d="M19 5l-9 14h7l-2 10 9-14h-7z" fill="#e30613"/></svg>Electrical</div>
      <div class="service-tile">
        <svg width="34" height="34" viewBox="0 0 34 34"><rect x="4" y="4" width="26" height="8" rx="2" fill="#fff"/><path d="M8 12h18l-4 8H12z" fill="#fff"/><path d="M10 26h14M12 31h10" stroke="#fff" stroke-width="2"/></svg>Fire and Smoke</div>
      <div class="service-tile">
        <svg width="30" height="34" viewBox="0 0 30 34"><path d="M15 1l13 5v10c0 9-6 14-13 17C8 30 2 25 2 16V6z" fill="#fff"/><path d="M9 17l4 4 8-9" stroke="#e30613" stroke-width="3" fill="none"/></svg>Security</div>
      <div class="service-tile">
        <svg width="34" height="34" viewBox="0 0 34 34"><path d="M5 9a18 18 0 0 0 20 20z" fill="#fff"/><path d="M15 19l10-10M24 5a8 8 0 0 1 5 5" stroke="#fff" stroke-width="2" fill="none"/><path d="M10 26l-4 6h12l-4-6" fill="#fff"/></svg>TV</div>
      <div class="service-tile">
        <svg width="42" height="24" viewBox="0 0 42 24"><rect x="1" y="1" width="40" height="16" rx="2" fill="#fff"/><path d="M6 12h30" stroke="#e30613" stroke-width="1.5"/><path d="M8 20v3M16 20v3M24 20v3M32 20v3" stroke="#fff" stroke-width="1.5"/></svg>Heat Pumps</div>
    </div>
  </div>

  <section class="projects" role="img" aria-label="Dark close-up photograph of a technician working on an electrical switchboard"></section>
  <div class="ghost projects-ghost">Latest Project</div>
  <h2 class="heading projects-title">Latest Project</h2>
  <div class="project" style="left:154px;top:1545px" role="img" aria-label="Photo of a commercial car dealership building"></div>
  <div class="project-card">
    <div class="badge"></div>
    <h4>Riverside Motors - Revamp</h4>
    <p>Retro-Fit Old Site for Riverside Motors - Complete electrical fit-out of retail...</p>
  </div>
  <div class="project" style="left:717px;top:1545px" role="img" aria-label="Photo of a commercial car dealership building"></div>
  <div class="project" style="left:154px;top:1753px;background:linear-gradient(180deg,#d6dde4 0%,#c4c8c6 45%,#8f8a78 62%,#7f9a4e 100%)" role="img" aria-label="Photo of new residential homes behind a lawn"></div>
  <div class="project" style="left:436px;top:1753px;background:linear-gradient(180deg,#dfe6ec 0%,#e4e4e4 30%,#b83a3a 60%,#777 100%)" role="img" aria-label="Photo of a retail shopfront"></div>
  <div class="project" style="left:717px;top:1753px;background:linear-gradient(180deg,#c9d3dc 0%,#e8e8e8 35%,#6d6d6d 62%,#555 100%)" role="img" aria-label="Photo of a white commercial building with car park"></div>

  <div class="newsletter-head">
    <h3>Newsletter</h3>
    <p>Lorem Ipsum is simply dummy text of the printing.</p>
  </div>
  <div class="newsletter-field">Enter Your E-mail
    <span class="send"><svg width="14" height="14" viewBox="0 0 14 14"><path d="M0 6l14-6-5 14-2-6z" fill="#fff"/></svg></span>
  </div>

  <footer class="footer">
    <div class="logo-box"><div class="logo"><span class="mark"></span>Brantwood Power</div></div>
    <p class="footer-about">Brantwood Power is a leading electrical installation and maintenance company based in Wanganui, but servicing all New Zealand. With over 15 professionally qualified and experienced Wanganui electricians, technicians and support staff we are leading the way in providing quality electrical services. Brantwood Power was established in 1991.</p>
    <div class="contact" style="left:154px">
      <svg width="18" height="16" viewBox="0 0 18 16"><path d="M9 0L0 8h3v8h4v-5h4v5h4V8h3z" fill="#9a9a9a"/></svg>
      <div>ADDRESS :<br>14 Kestrel Street, Wanganui 4500</div>
    </div>
    <div class="contact" style="left:379px">
      <svg width="16" height="16" viewBox="0 0 16 16"><path d="M3 0l3 4-2 2c1 2 4 5 6 6l2-2 4 3-2 3C7 16 0 9 0 3z" fill="#9a9a9a"/></svg>
      <div>0800 55 21 40<br>(06) 344 7120</div>
    </div>
    <div class="contact" style="left:572px">
      <svg width="18" height="14" viewBox="0 0 18 14"><path d="M0 5l9-5 9 5v9H0z" fill="#9a9a9a"/><path d="M1 5l8 5 8-5" stroke="#3a3a3a" fill="none" stroke-width="1.3"/></svg>
      <div>EMAIL :<br>office@brantwoodpower.co.nz</div>
    </div>
    <div class="footer-social"><span></span><span></span><span></span><span></span></div>
    <div class="quick-title">QUICK LINKS</div>
    <ul class="links" style="left:154px"><li>Residential Electrical</li><li>Commercial Electrical</li><li>Ductless Heat Pumps</li><li>Fire Alarms</li><li>Security Cameras</li></ul>
    <ul class="links" style="left:335px"><li>Hot Water Cylinders</li><li>CCTV Cameras</li><li>Interior Lighting</li><li>Exterior Lighting</li><li>Smoke Detectors</li></ul>
    <ul class="links" style="left:504px"><li>Air Conditioners</li><li>Free to View TV</li><li>Satellite Dish</li><li>UFH Aerials</li><li>Home Security</li></ul>
    <ul class="links" style="left:663px"><li>Electrical Inspections</li><li>Ventilation</li><li>Hot Water Heatpumps</li><li>Heat Recovery Systems</li><li>Thermal Imaging</li></ul>
    <ul class="links" style="left:853px"><li>Appliance repairs</li><li>Electrical testing &amp; tagging</li><li>Phone and Data</li></ul>
  </footer>
  <div class="copyright"><span>Copyright 2018 © Brantwood Power. All Rights Reserved.</span><span>Terms and Condition</span></div>
</div>

<div class="abs device-heading"><span>DEVICE VIEW</span></div>
</body>
</html>
```